New clean and fresh corporate PPT template for Telecom equipment maker

KRV (BORVEX KRVT) is a telecom equipment maker in Silicon Valley. Our current PPT template that goes with http://melikport.com is overbuilt, dark, huge in file size, and looks the opposite of fresh and clean.
Our new microsite @ http://investor-krvt.com is the direction we want to go. We are B2B, selling to telecom operators, but still want something that looks clean and fresh and not stuffy, hence primarily white background with maximum whitespace in 16:9 format.
Style guidelines attached, exclusive use of approved colors required, the master should remain as simple as possible, and we want the file size to stay reasonable (i.e. less is better). Features we would like include:
- Lato font built-in to the template
- Text boxes with standard size fonts, that automatically get smaller with indention
- An interesting bullet style, nothing crazy, but with visual interest
- A pre-selected table format that is clean and allows for high-density tables with many rows & columns
- Whichever standard slides layouts in the master you think would help result in slides that are found in the current deck, without someone needing to build their own slide

```html
<!DOCTYPE html>
<html lang="en">
<head>
<meta charset="utf-8">
<title>POL in Hospitality</title>
<link href="https://fonts.googleapis.com/css2?family=Lato:ital,wght@0,400;0,700;1,400&family=Arimo:wght@700&display=swap" rel="stylesheet">
<style>
  :root {
    --title: #4b5a6b;
    --body: #555b61;
    --label-red: #c00000;
    --frame-blue: #2f62e6;
    --quad-dark: #4a4a4a;
    --ring: #dadada;
    --teal: #3cc6c6;
    --green: #7ac943;
    --coral: #f26363;
    --muted: #9a9a9a;
  }
  * { margin: 0; padding: 0; box-sizing: border-box; }
  html, body { width: 1200px; height: 675px; overflow: hidden; background: #fff; }
  .slide { position: relative; width: 1200px; height: 675px; font-family: "Lato", sans-serif; color: var(--body); }

  .slide-title { position: absolute; top: 36px; left: 0; width: 1200px; text-align: center; font-size: 44px; font-weight: 400; color: var(--title); letter-spacing: -0.5px; }
  .title-rule { position: absolute; top: 101px; left: 537px; display: flex; height: 4px; }
  .title-rule span { width: 42px; height: 4px; }
  .title-rule .teal { background: var(--teal); }
  .title-rule .green { background: var(--green); }
  .title-rule .coral { background: var(--coral); }

  .service { position: absolute; width: 206px; left: 0; text-align: center; }
  .service-thumb { width: 80px; height: 80px; margin: 0 auto; border-radius: 50%; border: 2px solid var(--frame-blue); box-shadow: 0 2px 4px rgba(0,0,0,.25); }
  .service-label { margin-top: 3px; font-family: "Arimo", sans-serif; font-weight: 700; font-size: 13px; color: var(--label-red); }

  .lobby-photo { position: absolute; left: 207px; top: 138px; width: 438px; height: 324px; border-radius: 38px; border: 2px solid var(--frame-blue); background: linear-gradient(160deg, #c9c3b6 0%, #9e968a 45%, #6b6257 75%, #4e6a63 100%); box-shadow: 0 2px 5px rgba(0,0,0,.2); }

  .benefit-cycle { position: absolute; left: 666px; top: 139px; }

  .client { position: absolute; left: 990px; width: 200px; text-align: center; font-size: 26px; font-weight: 700; color: var(--title); }

  .testimonial { position: absolute; left: 245px; top: 488px; width: 720px; font-size: 23.5px; line-height: 28px; color: var(--body); letter-spacing: -0.4px; }
  .attribution { position: absolute; left: 354px; top: 573px; font-size: 23px; font-style: italic; color: var(--body); }

  .brand { position: absolute; left: 16px; top: 624px; display: flex; align-items: center; gap: 8px; }
  .brand-mark { width: 12px; height: 12px; background: var(--muted); }
  .brand-name { font-size: 34px; font-weight: 700; color: var(--muted); letter-spacing: 1px; line-height: 1; }
  .brand-tagline { margin-left: 6px; font-size: 10px; line-height: 12px; color: #b5b5b5; letter-spacing: .5px; }

  .copyright { position: absolute; top: 643px; left: 0; width: 1200px; text-align: center; font-size: 14px; color: var(--muted); }
  .page-rule { position: absolute; left: 1126px; top: 623px; width: 74px; height: 4px; background: var(--teal); }
  .page-number { position: absolute; left: 1128px; top: 634px; font-size: 20px; color: var(--title); }
</style>
</head>
<body>
<main class="slide">
  <h1 class="slide-title">POL in Hospitality</h1>
  <div class="title-rule"><span class="teal"></span><span class="green"></span><span class="coral"></span></div>

  <div class="service" style="top:100px"><div class="service-thumb" role="img" aria-label="Ceiling security camera" style="background:radial-gradient(circle,#ececec,#a9b2bb)"></div><div class="service-label">Security Cameras</div></div>
  <div class="service" style="top:204px"><div class="service-thumb" role="img" aria-label="Hand holding a TV remote" style="background:radial-gradient(circle,#5a4a44,#1e2a3a)"></div><div class="service-label">TV, Video</div></div>
  <div class="service" style="top:304px"><div class="service-thumb" role="img" aria-label="Group of smartphones" style="background:radial-gradient(circle,#8a8a8a,#2c2c2c)"></div><div class="service-label">Hi Capacity Wi-Fi</div></div>
  <div class="service" style="top:406px"><div class="service-thumb" role="img" aria-label="Open-plan back office" style="background:radial-gradient(circle,#c8c2b4,#5e5a52)"></div><div class="service-label">Back Office</div></div>
  <div class="service" style="top:505px"><div class="service-thumb" role="img" aria-label="Hotel door with keycard lock" style="background:radial-gradient(circle,#6e6862,#1d1a18)"></div><div class="service-label">Access Control / BMS</div></div>

  <div class="lobby-photo" role="img" aria-label="Multi-storey hotel atrium lobby with balconies and a fountain"></div>

  <svg class="benefit-cycle" width="330" height="320" viewBox="0 0 330 320" aria-label="Benefits cycle">
    <g fill="var(--ring)">
      <g id="ring-arrow">
        <path d="M20 152 A145 145 0 0 1 151 15" fill="none" stroke="var(--ring)" stroke-width="13"/>
        <polygon points="149,-1 149,31 164,15"/>
      </g>
      <use href="#ring-arrow" transform="rotate(90 165 160)"/>
      <use href="#ring-arrow" transform="rotate(180 165 160)"/>
      <use href="#ring-arrow" transform="rotate(270 165 160)"/>
    </g>
    <g fill="var(--quad-dark)">
      <path d="M160 155 L35 155 A125 125 0 0 1 160 30 Z"/>
      <path d="M170 155 L170 30 A125 125 0 0 1 295 155 Z"/>
      <path d="M170 165 L295 165 A125 125 0 0 1 170 290 Z"/>
      <path d="M160 165 L160 290 A125 125 0 0 1 35 165 Z"/>
    </g>
    <g fill="#f2f2f2" font-family="Lato, sans-serif" font-size="19" text-anchor="middle">
      <text x="102" y="108">Save</text><text x="102" y="132">Money</text>
      <text x="230" y="108">Free Up</text><text x="230" y="132">Space</text>
      <text x="102" y="202">Guest</text><text x="102" y="226">Experience</text>
      <text x="230" y="202">Future</text><text x="230" y="226">Proof</text>
    </g>
  </svg>

  <div class="client" style="top:143px">Alderwell</div>
  <div class="client" style="top:220px">Brightmoor</div>
  <div class="client" style="top:356px">The Halvering</div>
  <div class="client" style="top:424px">Corvessa</div>

  <p class="testimonial">“We chose KRV POL because of its small footprint, high-bandwidth, low disruption to guests and its lifespan of more than 25 years – we need a solution that doesn’t have to be replace in the near future”</p>
  <p class="attribution">Martin Avery, CIO, Seabrook Hospitality</p>

  <div class="brand">
    <span class="brand-mark"></span>
    <span class="brand-name">KRV</span>
    <span class="brand-tagline">NETWORKS THAT<br>KEEP PACE</span>
  </div>
  <p class="copyright">© 2018 Korvane Networks – Proprietary and Confidential</p>
  <div class="page-rule"></div>
  <p class="page-number">19</p>
</main>
</body>
</html>
```